card design for engineering consultancy

engineering drafting and project management company the provides drafting services for.
Electrical, Hydraulic, Mechanical, and Civil services
The company is called K7R Services and logo is as attached
Information on card should be.
1. Logo
2.website : K7RServices.com
3. email : info@K7RServices.com
4. Phone: (+61) 400512738
5. Motto: Design - Document - Develop - Deliver

this card should be basically used for business identification only

Target Market(s)

electricians plumbers air conditioning installers and civil contractors

Industry/Entity Type

engineering, drafting, electrical, plumbing, airconditioning, civil

Contact Information for Business Card

1. Logo 2.website : K7RServices.com 3. email : info@K7RServices.com 4. Phone: (+61) 400512738 5. Motto: Design - Document - Develop - Deliver

Font styles to use
Serif

Requirements
Must have
• logo
Nice to have
• something inovative and different that makes it stand out from being just another business card

```html
<!DOCTYPE html>
<html lang="en">
<head>
<meta charset="utf-8">
<title>K7R Services – Business Card</title>
<link href="https://fonts.googleapis.com/css2?family=Cinzel:wght@500;600;700&family=Montserrat:wght@400;500;600&display=swap" rel="stylesheet">
<style>
  :root {
    --page-bg: #e6e4e1;
    --card-dark-top: #3b3b3c;
    --card-dark-bottom: #1f1f20;
    --card-light: #ffffff;
    --ink-dark: #2e2e30;
    --ink-grey: #555658;
    --mark-grey: #8a8b8d;
    --accent-red: #d3202f;
    --band-grey: #404042;
    --white: #ffffff;
  }
  * { margin: 0; padding: 0; box-sizing: border-box; }
  html, body {
    width: 1200px; height: 900px; overflow: hidden;
    background: var(--page-bg);
  }
  .stage { position: relative; width: 1200px; height: 900px; }

  .card {
    position: absolute;
    width: 630px; height: 360px;
    border-radius: 24px;
    overflow: hidden;
    box-shadow: 0 14px 30px rgba(0,0,0,.22);
  }

  /* Front (dark) card */
  .card-front {
    left: 150px; top: 55px;
    background: linear-gradient(160deg, var(--card-dark-top), var(--card-dark-bottom));
  }
  .front-brand {
    position: absolute; left: 0; right: 0; top: 118px;
    display: flex; justify-content: center; align-items: center; gap: 16px;
  }
  .brand-square { width: 22px; height: 22px; background: var(--accent-red); }
  .front-brand .brand-name {
    font-family: "Cinzel", serif; font-weight: 600;
    font-size: 50px; letter-spacing: 4px; color: var(--mark-grey);
  }
  .front-motto {
    position: absolute; left: 0; right: 0; top: 240px;
    text-align: center;
    font-family: "Montserrat", sans-serif; font-weight: 600;
    font-size: 17px; letter-spacing: .5px; color: var(--white);
  }
  .front-motto .sep { color: var(--accent-red); margin: 0 10px; font-weight: 500; }

  /* Back (white) card */
  .card-back {
    left: 420px; top: 495px;
    background: var(--card-light);
  }
  .back-brand {
    position: absolute; left: 44px; top: 56px;
    display: flex; align-items: center; gap: 12px;
  }
  .back-brand .brand-square { width: 18px; height: 18px; }
  .back-brand .brand-name {
    font-family: "Cinzel", serif; font-weight: 600;
    font-size: 34px; letter-spacing: 2px; color: var(--ink-grey);
  }
  .motto-list {
    position: absolute; right: 40px; top: 44px;
    list-style: none;
    font-family: "Cinzel", serif; font-weight: 500;
    font-size: 20px; letter-spacing: 3px; color: var(--ink-dark);
    text-align: right; line-height: 30px;
  }
  .motto-list li { display: flex; justify-content: flex-end; align-items: center; gap: 8px; }
  .motto-list svg { width: 16px; height: 16px; flex: none; }

  .holder-name {
    position: absolute; left: 44px; top: 150px;
    font-family: "Cinzel", serif; font-weight: 700;
    font-size: 30px; letter-spacing: 1px; color: var(--ink-dark);
  }
  .holder-name .surname { color: var(--accent-red); }

  .contact-list {
    position: absolute; left: 46px; top: 200px;
    list-style: none;
    font-family: "Montserrat", sans-serif; font-weight: 400;
    font-size: 16px; color: var(--ink-dark); line-height: 27px;
  }
  .contact-list li { display: flex; align-items: center; gap: 10px; }
  .contact-list svg { width: 14px; height: 14px; flex: none; }
  .contact-list .web-domain { color: var(--accent-red); }

  .back-bands { position: absolute; left: 0; bottom: 0; width: 630px; height: 100px; }
</style>
</head>
<body>
<main class="stage">

  <section class="card card-front" aria-label="Business card front">
    <div class="front-brand">
      <span class="brand-square"></span>
      <span class="brand-name">K7R Services</span>
    </div>
    <p class="front-motto">DESIGN<span class="sep">|</span>DOCUMENT<span class="sep">|</span>DEVELOP<span class="sep">|</span>DELIVER</p>
  </section>

  <section class="card card-back" aria-label="Business card back">
    <div class="back-brand">
      <span class="brand-square"></span>
      <span class="brand-name">K7R Services</span>
    </div>

    <ul class="motto-list">
      <li><svg viewBox="0 0 16 16"><circle cx="8" cy="8" r="7" fill="none" stroke="var(--accent-red)" stroke-width="2"/><path d="M6 4.8 L11 8 L6 11.2Z" fill="var(--accent-red)"/></svg>Design</li>
      <li><svg viewBox="0 0 16 16"><circle cx="8" cy="8" r="7" fill="none" stroke="var(--accent-red)" stroke-width="2"/><path d="M6 4.8 L11 8 L6 11.2Z" fill="var(--accent-red)"/></svg>Document</li>
      <li><svg viewBox="0 0 16 16"><circle cx="8" cy="8" r="7" fill="none" stroke="var(--accent-red)" stroke-width="2"/><path d="M6 4.8 L11 8 L6 11.2Z" fill="var(--accent-red)"/></svg>Develop</li>
      <li><svg viewBox="0 0 16 16"><circle cx="8" cy="8" r="7" fill="none" stroke="var(--accent-red)" stroke-width="2"/><path d="M6 4.8 L11 8 L6 11.2Z" fill="var(--accent-red)"/></svg>Deliver</li>
    </ul>

    <h1 class="holder-name">Daniel <span class="surname">Reeve</span></h1>

    <ul class="contact-list">
      <li><svg viewBox="0 0 14 14"><path d="M3 1 L5.5 1 L6.3 4 L4.7 5.2 C5.4 6.8 6.8 8.4 8.6 9.3 L9.8 7.7 L13 8.5 L13 11 C13 12.2 12 13 10.8 12.9 C5.5 12.2 1.6 8.3 1 3.2 C0.9 2 1.8 1 3 1Z" fill="var(--accent-red)"/></svg>(+61) 400512738</li>
      <li><svg viewBox="0 0 14 14"><rect x="1" y="3" width="12" height="8.5" fill="none" stroke="var(--accent-red)" stroke-width="1.5"/><path d="M1.5 3.5 L7 8 L12.5 3.5" fill="none" stroke="var(--accent-red)" stroke-width="1.5"/></svg>info@K7RServices.com</li>
      <li><svg viewBox="0 0 14 14"><circle cx="7" cy="7" r="6" fill="none" stroke="var(--accent-red)" stroke-width="1.4"/><ellipse cx="7" cy="7" rx="2.6" ry="6" fill="none" stroke="var(--accent-red)" stroke-width="1.2"/><path d="M1 7 H13 M2 4 H12 M2 10 H12" stroke="var(--accent-red)" stroke-width="1"/></svg>www.<span class="web-domain">K7RServices.com</span></li>
    </ul>

    <svg class="back-bands" viewBox="0 0 630 100" aria-hidden="true">
      <polygon points="0,82 362,40 344,100 0,100" fill="var(--accent-red)"/>
      <polygon points="376,38 630,8 630,100 358,100" fill="var(--band-grey)"/>
    </svg>
  </section>

</main>
</body>
</html>
```